Business Card for Dental Surgery

Professional and vibrant business card for dental surgery

Other side to incorporate space for appointment date and times

My website is www.tallowbydental.com.au

Target Market(s)

All

Industry/Entity Type

Dental

Requirements
Must have
• Catchy
Phone no, internet etc
Nice to have
• portray same image as website.
on reverse appointment side:
"Please give 24 hours notice if you cannot attend"
Nice colours

```html
<!DOCTYPE html>
<html lang="en">
<head>
<meta charset="utf-8">
<title>Tallowby Dental – Business Card Front</title>
<link rel="stylesheet" href="https://fonts.googleapis.com/css2?family=Questrial&family=Oswald:wght@300&display=swap">
<style>
  :root {
    --brand-purple: #8e2a8a;
    --nav-dark: #2b3335;
    --nav-text: #ffffff;
    --nav-highlight: #b7d434;
    --teal-light: #b0d8db;
    --teal-mid: #86b8ba;
    --teal-band: #4e7c7e;
    --teal-swoosh: #9fcbcd;
    --ink: #26383a;
    --brush-green: #a8cc2c;
    --tooth-tone: #e6f5f6;
    --page: #ffffff;
  }
  * { margin: 0; padding: 0; box-sizing: border-box; }
  html, body {
    width: 1200px; height: 900px; overflow: hidden;
    background: var(--page);
    font-family: "Questrial", "Century Gothic", sans-serif;
  }
  .canvas { position: relative; width: 1200px; height: 900px; }

  .card {
    position: absolute; left: 16px; top: 16px;
    width: 1168px; height: 728px;
    border: 4px solid var(--brand-purple);
    background: var(--page);
    overflow: hidden;
  }

  .brand-name {
    position: absolute; left: 0; right: 0; top: 52px;
    text-align: center;
    font-size: 66px; letter-spacing: -1px;
    color: var(--brand-purple);
  }

  .nav-bar {
    position: absolute; left: 0; right: 0; top: 168px; height: 48px;
    background: var(--nav-dark);
    display: flex; align-items: center;
  }
  .nav-item {
    position: absolute; transform: translateX(-50%);
    white-space: nowrap;
    font-size: 22px; color: var(--nav-text);
  }
  .nav-item.is-current { color: var(--nav-highlight); font-weight: 700; font-size: 24px; letter-spacing: 0.5px; }

  .info-panel {
    position: absolute; left: 0; right: 0; top: 226px; bottom: 0;
  }
  .info-panel svg.backdrop { position: absolute; inset: 0; width: 100%; height: 100%; }

  .address {
    position: absolute; left: 0; right: 0; top: 30px;
    text-align: center; color: var(--ink);
    font-size: 62px; line-height: 80px;
  }
  .brush-stroke {
    position: absolute; left: 340px; top: 248px;
    width: 520px; height: 10px; border-radius: 5px;
    background: var(--brush-green);
  }
  .phone {
    position: absolute; left: 0; right: 0; top: 280px;
    text-align: center; color: var(--ink);
    font-size: 54px; word-spacing: 14px; letter-spacing: 2px;
  }
  .web-band {
    position: absolute; left: 0; right: 0; top: 380px; height: 56px;
    display: flex; align-items: center; justify-content: center;
    padding-right: 120px;
    font-size: 34px; color: var(--nav-text);
  }
  .tooth-art {
    position: absolute; left: 930px; top: 264px;
    width: 236px; height: 232px;
    border-radius: 70px 70px 50px 50px;
    background: linear-gradient(160deg, var(--tooth-tone), #cfe6e8);
  }

  .side-label {
    position: absolute; left: 0; right: 0; top: 776px;
    text-align: center;
    font-family: "Oswald", "Arial Narrow", sans-serif;
    font-weight: 300; font-size: 84px; line-height: 96px;
    color: var(--brand-purple);
  }
</style>
</head>
<body>
<div class="canvas">
  <section class="card">
    <h1 class="brand-name">Tallowby Dental</h1>

    <nav class="nav-bar">
      <span class="nav-item" style="left:166px">General Dentistry</span>
      <span class="nav-item" style="left:360px">Cosmetic Dentistry</span>
      <span class="nav-item is-current" style="left:578px">CONTACT US</span>
      <span class="nav-item" style="left:808px">Preventive Dentistry</span>
      <span class="nav-item" style="left:1036px">Speacialized Service</span>
    </nav>

    <div class="info-panel">
      <svg class="backdrop" viewBox="0 0 1168 498" preserveAspectRatio="none" aria-hidden="true">
        <rect width="1168" height="498" fill="var(--teal-light)"/>
        <polygon points="0,410 1168,80 1168,498 0,498" fill="var(--teal-mid)"/>
        <rect x="0" y="380" width="1168" height="56" fill="var(--teal-band)"/>
        <path d="M0,436 C300,470 700,498 1168,440 L1168,498 L0,498 Z" fill="var(--teal-swoosh)"/>
      </svg>

      <p class="address">18 Tallowby Street<br>Tallowby NSW 2199</p>
      <div class="brush-stroke" role="img" aria-label="Green toothbrush stroke illustration"></div>
      <p class="phone">0 2 9481 3725</p>
      <p class="web-band">www.tallowbydental.com.au</p>
      <div class="tooth-art" role="img" aria-label="Stylised white tooth illustration"></div>
    </div>
  </section>

  <p class="side-label">FRONT</p>
</div>
</body>
</html>
```